Crestwell Renewal Business Card Design Phase 2

Professional and clean design. The design colors should flow with the logo. Two-sided card with the website on the back which is:

www.CrestwellRenewal.example.

"Specializing in Water Damage Restoration"

On the front I need the name, email, phone, and logo.

Name: Dorian Halvek
Email: Dorian@CrestwellRenewal.example
Phone: 555-318-2046 for now

I only have the Preview and Thumbnail right now but should have the source files uploaded within a day or two.

Target Market(s)

Flood victims, home owners with water damage from busted pipes etc...

Industry/Entity Type

Business

Contact Information for Business Card

Name: Dorian Halvek

Font styles to use
Serif
Sans Serif

Requirements
Must have
• Business Card Details Info

```html
<!DOCTYPE html>
<html lang="en">
<head>
<meta charset="utf-8">
<title>Crestwell Renewal – Business Card</title>
<link href="https://fonts.googleapis.com/css2?family=Open+Sans:wght@400;600;700;800&display=swap" rel="stylesheet">
<style>
  :root {
    --stage: #e8e5df;
    --card-white: #ffffff;
    --brand-blue: #1f3f8f;
    --brand-green: #4fa845;
    --green-light: #66bb5a;
    --green-dark: #3b8f34;
    --text-grey: #4a4f57;
    --white: #ffffff;
  }
  * { box-sizing: border-box; margin: 0; padding: 0; }
  html, body {
    width: 1200px; height: 780px; overflow: hidden;
    background: var(--stage);
    font-family: "Open Sans", Arial, sans-serif;
  }
  .stage {
    width: 1200px; height: 780px;
    display: flex; align-items: center; justify-content: center; gap: 40px;
  }
  .card {
    width: 540px; height: 309px; position: relative;
    box-shadow: 0 10px 26px rgba(0,0,0,.18);
    overflow: hidden;
  }
  /* Front */
  .card--front { background: var(--card-white); }
  .front__name {
    position: absolute; top: 34px; right: 36px;
    color: var(--brand-blue); font-weight: 700; font-size: 22px;
  }
  .front__brand { position: absolute; left: 36px; top: 96px; }
  .brand-name {
    color: var(--brand-blue); font-weight: 800; text-transform: uppercase;
    font-size: 40px; line-height: 1; letter-spacing: -0.5px;
    display: flex; align-items: center; gap: 10px;
  }
  .brand-dot { width: 14px; height: 14px; border-radius: 50%; background: var(--brand-blue); flex: none; }
  .front__tagline {
    margin-top: 10px; color: var(--brand-green); font-size: 13.5px; font-weight: 600;
  }
  .front__contacts {
    position: absolute; left: 36px; bottom: 28px;
    list-style: none; display: flex; flex-direction: column; gap: 6px;
  }
  .contact { display: flex; align-items: center; gap: 10px; color: var(--text-grey); font-size: 14px; }
  .contact__icon {
    width: 18px; height: 18px; background: var(--brand-green); border-radius: 2px;
    display: flex; align-items: center; justify-content: center; flex: none;
  }
  /* Back */
  .card--back {
    background: radial-gradient(ellipse at 55% 40%, var(--green-light) 0%, var(--brand-green) 45%, var(--green-dark) 100%);
    color: var(--white);
  }
  .back__info {
    position: absolute; left: 40px; top: 40px; bottom: 40px;
    display: flex; flex-direction: column; justify-content: center; gap: 10px;
  }
  .back__rule { width: 150px; height: 1px; background: rgba(255,255,255,.8); }
  .back__tagline { font-size: 13px; font-weight: 600; }
  .back__web { font-size: 13px; }
  .back__brand {
    position: absolute; right: 38px; top: 50%; transform: translateY(-50%);
  }
  .back__brand .brand-name { color: var(--white); font-size: 34px; flex-direction: column; align-items: flex-end; gap: 2px; }
</style>
</head>
<body>
<main class="stage">
  <section class="card card--front" aria-label="Business card front">
    <p class="front__name">Dorian Halvek</p>
    <div class="front__brand">
      <p class="brand-name"><span class="brand-dot"></span>Crestwell Renewal</p>
      <p class="front__tagline">Specializing in Water Damage Restoration</p>
    </div>
    <ul class="front__contacts">
      <li class="contact">
        <span class="contact__icon"><svg width="12" height="12" viewBox="0 0 24 24"><path fill="#fff" d="M6.6 10.8a15 15 0 0 0 6.6 6.6l2.2-2.2c.3-.3.7-.4 1-.2 1.1.4 2.3.6 3.6.6.6 0 1 .4 1 1V20c0 .6-.4 1-1 1A17 17 0 0 1 3 4c0-.6.4-1 1-1h3.5c.6 0 1 .4 1 1 0 1.3.2 2.5.6 3.6.1.3 0 .7-.2 1z"/></svg></span>
        555-318-2046
      </li>
      <li class="contact">
        <span class="contact__icon"><svg width="12" height="12" viewBox="0 0 24 24"><rect x="2" y="5" width="20" height="14" fill="none" stroke="#fff" stroke-width="2"/><path d="M2 5l10 8 10-8" fill="none" stroke="#fff" stroke-width="2"/></svg></span>
        Dorian@CrestwellRenewal.example
      </li>
      <li class="contact">
        <span class="contact__icon"><svg width="12" height="12" viewBox="0 0 24 24" fill="none" stroke="#fff" stroke-width="2"><circle cx="12" cy="12" r="9"/><path d="M3 12h18M12 3c3 3 3 15 0 18M12 3c-3 3-3 15 0 18"/></svg></span>
        www.CrestwellRenewal.example
      </li>
    </ul>
  </section>

  <section class="card card--back" aria-label="Business card back">
    <div class="back__info">
      <span class="back__rule"></span>
      <p class="back__tagline">Specializing in Water Damage Restoration</p>
      <p class="back__web">www.CrestwellRenewal.example</p>
      <span class="back__rule"></span>
    </div>
    <div class="back__brand">
      <p class="brand-name"><span>Crestwell</span><span>Renewal</span></p>
    </div>
  </section>
</main>
</body>
</html>
```